Lark Meadow Designs Business Needs A Business Card Design

We are in need of a Logo design and business card design for a new small business called Lark Meadow Designs. We create party decorations and favours for Bridal Showers, Baby Showers, Weddings Birthdays etc. This is a very personalized service based on Clients theme, colour, and style. We are looking for a high end elegant look. I have attached a file to the style I like including the type of paper.

Target Market(s)

women, young adults, expectant mothers, mothers

Industry/Entity Type

Small Business

Contact Information for Business Card

Lark Meadow Designs Essex, ON 519-608-1942 larkmeadowdesigns.ca dana@larkmeadowgiftwrapping.com find us on Friendlink

Logo Text

Lark Meadow Designs

Font styles to use
Script

Requirements
Must have
• Name, email, web address, phone number
Should not have
• cutesy graphics

```html
<!DOCTYPE html>
<html lang="en">
<head>
<meta charset="utf-8">
<title>Lark Meadow Designs – Business Card</title>
<link rel="stylesheet" href="https://fonts.googleapis.com/css2?family=Dancing+Script:wght@500;700&family=Open+Sans:wght@400&display=swap">
<style>
  :root {
    --backdrop: #d6d4cf;
    --card-paper: #e4e6de;
    --card-paper-shade: #d9dcd2;
    --wash: rgba(150, 152, 144, 0.22);
    --ink: #3b3e3b;
    --ink-soft: #585b57;
  }
  * { margin: 0; padding: 0; box-sizing: border-box; }
  html, body {
    width: 1200px; height: 873px; overflow: hidden;
    background: var(--backdrop);
  }
  .sheet {
    position: relative; width: 1200px; height: 873px;
    display: flex; align-items: center; justify-content: center; gap: 80px;
  }
  .card {
    position: relative; width: 500px; height: 286px;
    background: linear-gradient(135deg, var(--card-paper), var(--card-paper-shade));
    box-shadow: 0 6px 18px rgba(0,0,0,0.18);
    color: var(--ink); overflow: hidden;
  }
  .brush-wash {
    position: absolute; left: 70px; top: 20px; width: 200px; height: 150px;
    background: radial-gradient(ellipse at center, var(--wash), transparent 70%);
  }
  .dotted-rule {
    position: absolute; height: 0;
    border-top: 3px dotted var(--ink);
  }
  .script {
    font-family: "Dancing Script", cursive; font-weight: 700;
    white-space: nowrap; line-height: 1;
  }
  /* Front */
  .front .rule-top { left: 40px; right: 40px; top: 48px; }
  .front .rule-bottom { left: 40px; right: 40px; top: 204px; }
  .front .wordmark {
    position: absolute; left: 0; right: 0; top: 62px; text-align: center;
    color: var(--ink);
  }
  .front .wordmark-lead {
    display: block; font-size: 32px; font-weight: 500; margin-bottom: 4px;
  }
  .front .wordmark-main { display: block; font-size: 86px; }
  .front .website {
    position: absolute; left: 40px; top: 222px;
    font-family: "Dancing Script", cursive; font-weight: 500;
    font-size: 22px; color: var(--ink-soft);
  }
  /* Back */
  .back .holder-name {
    position: absolute; left: 34px; top: 22px; font-size: 34px;
  }
  .back .rule-name { left: 34px; width: 250px; top: 66px; }
  .back .contact-list { position: absolute; left: 34px; top: 80px; list-style: none; }
  .back .contact-label {
    font-family: "Dancing Script", cursive; font-weight: 500;
    font-size: 18px; color: var(--ink-soft); line-height: 1.1;
  }
  .back .contact-value {
    font-family: "Open Sans", sans-serif; font-size: 11px; color: var(--ink);
    margin: 0 0 6px 14px; line-height: 1.35; white-space: nowrap;
  }
  .back .wordmark-small {
    position: absolute; right: 34px; top: 172px; text-align: right;
    color: var(--ink);
  }
  .back .wordmark-small .wordmark-lead {
    display: block; font-size: 18px; font-weight: 500; margin-bottom: 2px;
  }
  .back .wordmark-small .wordmark-main { display: block; font-size: 40px; }
  .back .rule-side { left: 34px; right: 34px; top: 246px; }
</style>
</head>
<body>
<main class="sheet">
  <section class="card front">
    <div class="brush-wash" role="img" aria-label="Faint grey brush-texture wash behind the name"></div>
    <div class="dotted-rule rule-top"></div>
    <h1 class="wordmark script">
      <span class="wordmark-lead">Lark Meadow</span>
      <span class="wordmark-main">Designs</span>
    </h1>
    <div class="dotted-rule rule-bottom"></div>
    <p class="website">www.larkmeadowdesigns.ca</p>
  </section>

  <section class="card back">
    <div class="brush-wash" role="img" aria-label="Faint grey brush-texture wash" style="left:240px;top:50px"></div>
    <h2 class="holder-name script">Dana Whitfield</h2>
    <div class="dotted-rule rule-name"></div>
    <ul class="contact-list">
      <li>
        <p class="contact-label">Address :</p>
        <p class="contact-value">Orchard Lane Studio Park Essex<br>P.O. Box 318 Essex, ON</p>
      </li>
      <li>
        <p class="contact-label">Phone :</p>
        <p class="contact-value">519-608-1942</p>
      </li>
      <li>
        <p class="contact-label">E-Mail :</p>
        <p class="contact-value">dana@larkmeadowgiftwrapping.com</p>
      </li>
    </ul>
    <p class="wordmark-small script">
      <span class="wordmark-lead">Lark Meadow</span>
      <span class="wordmark-main">Designs</span>
    </p>
    <div class="dotted-rule rule-side"></div>
  </section>
</main>
</body>
</html>
```